Northern Terrain Published Photographer Website

I need a website to feature a home page slide show of 6 of my top photos then a few simple pages including; gallery, bio, social, checkout, services
Updates

Need extra days to review

Target Market(s)

photography

Industry/Entity Type

Photographer

Coding

Coded - Design and coding required

Number of Pages Required

5+ page

Colors

Designer to choose colors to be used in the design.

Requirements
Must have
• clean eye catching elegant trendy
Nice to have
• unique and creative from other photographer websites

```html
<!DOCTYPE html>
<html lang="en">
<head>
<meta charset="utf-8">
<title>Elise Marwood Photography</title>
<link href="https://fonts.googleapis.com/css2?family=Poppins:wght@300;400;500;600&family=Bebas+Neue&family=Kaushan+Script&display=swap" rel="stylesheet">
<style>
:root{
  --ink:#111111;
  --white:#ffffff;
  --accent:#f2a516;
  --muted:#555555;
  --night:#15130f;
  --line:#cfcfcf;
}
*{margin:0;padding:0;box-sizing:border-box}
html,body{width:1200px;height:4289px;overflow:hidden}
body{position:relative;background:var(--white);font-family:'Poppins',sans-serif;color:var(--ink)}
.abs{position:absolute}
.script{font-family:'Kaushan Script',cursive}

/* hero */
.hero{left:0;top:0;width:1200px;height:599px;
  background:radial-gradient(ellipse at 55% 30%,#c48a1f 0%,#7a5214 35%,#2e1f0a 75%,#140d05 100%)}
.brand{left:95px;top:34px;display:flex;align-items:center;gap:12px;color:var(--white);font-size:26px;font-weight:400;letter-spacing:1px}
.brand-dot{width:16px;height:16px;border-radius:50%;background:var(--white)}
.hero-tools{right:100px;top:44px;display:flex;gap:36px;align-items:center}
.hero-tag{left:0;width:1200px;top:165px;text-align:center;color:var(--white);font-size:44px}
.hero-title{left:0;width:1200px;top:222px;text-align:center;color:var(--white);font-family:'Bebas Neue',sans-serif;font-size:118px;letter-spacing:2px;line-height:1}
.btn-outline{left:491px;top:366px;width:216px;height:58px;border:2px solid var(--white);color:var(--white);display:flex;align-items:center;justify-content:center;font-size:21px;font-weight:500}
.hero-social{left:92px;top:386px;display:flex;flex-direction:column;gap:10px;color:var(--white);font-size:8px}
.hero-social span{display:flex;align-items:center;gap:8px}
.hero-social i{display:block;width:9px;height:9px;border-radius:50%;background:var(--white)}
.hero-nav{left:1090px;top:406px;display:flex;flex-direction:column;gap:14px}

/* about */
.about-hi{left:95px;top:655px;font-size:29px;font-weight:300;color:#333}
.about-name{left:95px;top:690px;font-size:52px}
.about-text{left:511px;top:670px;width:590px;font-size:12.5px;line-height:21px;color:var(--muted)}
.video{left:0;top:775px;width:895px;height:521px;background:linear-gradient(135deg,#4d5436 0%,#2f3524 45%,#5c5a4c 70%,#3a3122 100%)}
.play{left:378px;top:966px}
.tagbar{left:918px;top:775px;width:62px;height:410px;background:var(--ink);color:var(--white);writing-mode:vertical-rl;display:flex;align-items:center;justify-content:center;font-size:20px;letter-spacing:3px}
.btn-dark{background:var(--ink);color:var(--white);display:flex;align-items:center;justify-content:center;font-weight:500;letter-spacing:2px}
.read-more{left:905px;top:1240px;width:200px;height:56px;font-size:19px}

/* headings */
.section-title{left:0;width:1200px;text-align:center;font-size:52px}
.underline{height:4px;background:var(--accent)}

/* portfolio */
.tile{height:337px}
.tile-hover{background:#1c1a22;color:var(--white);display:flex;flex-direction:column;align-items:center;justify-content:center;gap:18px;font-size:24px}
.view-all{left:526px;top:2155px;width:146px;height:48px;font-size:18px}

/* blog */
.post-img{width:536px;height:346px}
.post-title{font-size:30px;font-weight:500}
.post-date{font-size:15px;color:var(--accent);font-weight:500}
.post-text{width:450px;font-size:12px;line-height:20px;color:var(--muted)}
.post-btn{width:101px;height:28px;font-size:11px;font-weight:600}

/* feedback */
.feedback{left:0;top:3132px;width:1200px;height:487px;background:linear-gradient(180deg,#121212 0%,#1a1611 55%,#3a2413 80%,#1c130b 100%)}
.fb-title{left:0;width:1200px;top:3200px;text-align:center;color:var(--white);font-size:52px}
.fb-text{left:190px;width:820px;top:3300px;text-align:center;color:#dddddd;font-size:12px;line-height:23px}
.fb-name{left:0;width:1200px;top:3390px;text-align:center;color:var(--white);font-size:22px;font-weight:500}
.avatar{border-radius:50%;border:3px solid var(--accent)}

/* gallery strip */
.strip{top:3619px;width:300px;height:270px}
.strip-overlay{left:541px;top:3690px;width:118px;height:118px;background:rgba(60,60,60,.55)}

/* footer */
.footer-brand{left:0;width:1200px;top:3958px;display:flex;justify-content:center;align-items:center;gap:14px;font-size:40px;font-weight:400}
.footer-brand .brand-dot{background:var(--ink);width:20px;height:20px}
.subscribe{left:243px;top:4057px;width:712px;height:65px;border:1px solid #999;border-radius:33px;display:flex;align-items:center;padding-left:30px;font-size:12px;color:#888;gap:10px}
.subscribe-btn{left:775px;top:4063px;width:175px;height:53px;border-radius:27px;font-size:18px;letter-spacing:3px}
.social-dot{top:4151px;width:43px;height:43px;border-radius:50%}
.copyright{left:0;width:1200px;top:4216px;text-align:center;font-size:12px;color:#333}
.copyright b{font-weight:600}
</style>
</head>
<body>

<!-- hero -->
<section class="abs hero" role="img" aria-label="Golden sunset over a lake with old pier posts and a bird silhouette"></section>
<div class="abs brand"><span>Elise Marwood</span><span class="brand-dot"></span></div>
<div class="abs hero-tools">
  <svg width="22" height="22" viewBox="0 0 22 22" fill="none" stroke="#fff" stroke-width="2"><circle cx="9" cy="9" r="7"/><line x1="14" y1="14" x2="20" y2="20"/></svg>
  <svg width="26" height="20" viewBox="0 0 26 20" fill="#fff"><rect y="0" width="26" height="3"/><rect y="8" width="26" height="3"/><rect y="16" width="26" height="3"/></svg>
</div>
<div class="abs hero-tag script">Photography is my Passion</div>
<div class="abs hero-title">IT'S ALWAYS GREAT!</div>
<div class="abs btn-outline">CONTACT US</div>
<div class="abs hero-social">
  <span><i></i>Social</span><span><i></i></span><span><i></i></span><span><i></i></span><span><i></i></span>
</div>
<div class="abs hero-nav">
  <svg width="16" height="16" viewBox="0 0 16 16" fill="#fff"><polygon points="3,1 14,8 3,15"/></svg>
  <svg width="18" height="14" viewBox="0 0 18 14" fill="none" stroke="#fff" stroke-width="1.6"><line x1="1" y1="7" x2="16" y2="7"/><polyline points="10,1 16,7 10,13"/></svg>
  <svg width="18" height="14" viewBox="0 0 18 14" fill="none" stroke="#fff" stroke-width="1.6"><line x1="2" y1="7" x2="17" y2="7"/><polyline points="8,1 2,7 8,13"/></svg>
</div>

<!-- about -->
<div class="abs about-hi">Hi, my name is</div>
<div class="abs about-name script">Elise Marwood</div>
<p class="abs about-text">Lorem Ipsum is simply dummy text of the printing and typesetting industry. Lorem Ipsum has been the industry's standard dummy text ever since the 1500s, when an unknown printer took a galley of type and scrambled it to make a type specimen book.</p>
<div class="abs video" role="img" aria-label="Waterfall in a wooded gorge beneath a railway bridge"></div>
<svg class="abs play" width="140" height="140" viewBox="0 0 140 140" fill="none" stroke="#fff" stroke-width="5"><circle cx="70" cy="70" r="66"/><polygon points="54,42 100,70 54,98" stroke-linejoin="round"/></svg>
<div class="abs tagbar">ENTHUSIASM PHOTOGRAPHER</div>
<div class="abs btn-dark read-more">READ MORE</div>

<!-- portfolio -->
<h2 class="abs section-title script" style="top:1340px">Our Portfolio</h2>
<div class="abs underline" style="left:474px;top:1409px;width:122px"></div>
<div class="abs tile" style="left:0;top:1449px;width:393px;background:linear-gradient(180deg,#5a86c4 0%,#c9d6e6 40%,#5f6e74 70%,#2d3a44 100%)" role="img" aria-label="Snowy river reflecting clouds"></div>
<div class="abs tile tile-hover" style="left:393px;top:1449px;width:404px">
  <svg width="52" height="52" viewBox="0 0 52 52" fill="none" stroke="#fff" stroke-width="4" stroke-linecap="round"><path d="M22 30 L30 22"/><path d="M18 26 L12 32 a7 7 0 0 0 10 10 L28 36"/><path d="M34 26 L40 20 a7 7 0 0 0 -10 -10 L24 16"/></svg>
  <span>Photography</span>
</div>
<div class="abs tile" style="left:797px;top:1449px;width:403px;background:linear-gradient(180deg,#8ea0bd 0%,#a9a39c 40%,#7d5e48 75%,#4a3428 100%)" role="img" aria-label="Canyon ridges under a cloudy sky"></div>
<div class="abs tile" style="left:0;top:1786px;width:393px;background:linear-gradient(180deg,#2f3f5c 0%,#9a5a3c 45%,#b5502b 65%,#3c3630 100%)" role="img" aria-label="Canyon cliffs glowing at sunset"></div>
<div class="abs tile" style="left:393px;top:1786px;width:404px;background:linear-gradient(180deg,#6a2d6e 0%,#d4583d 45%,#8a2c60 70%,#2a1233 100%)" role="img" aria-label="Desert tree silhouette against a purple sunset"></div>
<div class="abs tile" style="left:797px;top:1786px;width:403px;background:linear-gradient(180deg,#b9b4a8 0%,#a55a35 40%,#3e6a5c 65%,#7a4028 100%)" role="img" aria-label="River bend around a red rock formation"></div>
<div class="abs btn-dark view-all">VIEW ALL</div>

<!-- blog -->
<h2 class="abs section-title script" style="top:2252px">Recent Blog</h2>
<div class="abs underline" style="left:482px;top:2313px;width:122px"></div>

<div class="abs post-img" style="left:93px;top:2358px;background:linear-gradient(180deg,#a9adb2 0%,#5d6670 45%,#3f7a84 65%,#b99a78 100%)" role="img" aria-label="Lake among desert bluffs under clouds"></div>
<h3 class="abs post-title" style="left:659px;top:2418px">Contrary to popular belief</h3>
<div class="abs post-date" style="left:659px;top:2460px">May 28 . 2019</div>
<p class="abs post-text" style="left:659px;top:2488px">Lorem Ipsum is simply dummy text of the printing and typesetting industry. Lorem Ipsum has been the industry's standard dummy text ever since the 1500s, when an unknown printer took a galley of type and scrambled it to make a type specimen book. It has survived not only five centuries, but also the leap into electronic typesetting, remaining essentially unchanged.</p>
<div class="abs btn-dark post-btn" style="left:659px;top:2606px">READ MORE</div>

<h3 class="abs post-title" style="left:97px;top:2790px">Contrary to popular belief</h3>
<div class="abs post-date" style="left:97px;top:2832px">May 28 . 2019</div>
<p class="abs post-text" style="left:97px;top:2860px">Lorem Ipsum is simply dummy text of the printing and typesetting industry. Lorem Ipsum has been the industry's standard dummy text ever since the 1500s, when an unknown printer took a galley of type and scrambled it to make a type specimen book. It has survived not only five centuries, but also the leap into electronic typesetting, remaining essentially unchanged.</p>
<div class="abs btn-dark post-btn" style="left:97px;top:2978px">READ MORE</div>
<div class="abs post-img" style="left:572px;top:2727px;background:linear-gradient(180deg,#8a7fa8 0%,#6d86b4 45%,#4c5e8c 70%,#3a3f66 100%)" role="img" aria-label="Snowy mountain range under a pastel sky"></div>

<!-- feedback -->
<section class="abs feedback" role="img" aria-label="Dark desert butte at dusk"></section>
<h2 class="abs fb-title script">Clients Feedback</h2>
<p class="abs fb-text">Lorem Ipsum is simply dummy text of the printing and typesetting industry. Lorem Ipsum has been the industry's standard dummy text ever since the 1500s, when an unknown printer took a galley of type and scrambled it to make a type specimen book. It has survived not only five centuries, but also the leap into electronic typesetting, remaining essentially unchanged.</p>
<svg class="abs" style="left:92px;top:3328px" width="28" height="20" viewBox="0 0 28 20" fill="none" stroke="#fff" stroke-width="2.4"><line x1="3" y1="10" x2="27" y2="10"/><polyline points="11,2 3,10 11,18"/></svg>
<svg class="abs" style="left:1083px;top:3328px" width="28" height="20" viewBox="0 0 28 20" fill="none" stroke="#fff" stroke-width="2.4"><line x1="1" y1="10" x2="25" y2="10"/><polyline points="17,2 25,10 17,18"/></svg>
<div class="abs fb-name">Lorem Ipsum</div>
<div class="abs avatar" style="left:497px;top:3463px;width:64px;height:64px;background:#8b7a6c" role="img" aria-label="Client portrait"></div>
<div class="abs avatar" style="left:639px;top:3463px;width:64px;height:64px;background:#9a8676" role="img" aria-label="Client portrait"></div>
<div class="abs avatar" style="left:555px;top:3451px;width:90px;height:90px;background:#a08c7c" role="img" aria-label="Client portrait"></div>

<!-- gallery strip -->
<div class="abs strip" style="left:0;background:linear-gradient(180deg,#7d5a48 0%,#9b7a62 50%,#5e4a3a 100%)" role="img" aria-label="Bighorn sheep grazing in the desert"></div>
<div class="abs strip" style="left:300px;background:linear-gradient(180deg,#4f6f9a 0%,#d48f3a 40%,#a0612c 70%,#6e5a44 100%)" role="img" aria-label="Rock butte reflected in still water"></div>
<div class="abs strip" style="left:600px;background:linear-gradient(180deg,#2a4e8c 0%,#6a88b8 40%,#e0a04a 60%,#5a3b2c 100%)" role="img" aria-label="Sunburst through a canyon arch"></div>
<div class="abs strip" style="left:900px;background:linear-gradient(180deg,#d97c16 0%,#f0a632 40%,#8a4a10 70%,#3a1d08 100%)" role="img" aria-label="Pier posts in a golden sunset"></div>
<div class="abs strip-overlay"></div>

<!-- footer -->
<div class="abs footer-brand"><span>Elise Marwood</span><span class="brand-dot"></span></div>
<div class="abs subscribe">
  <svg width="14" height="10" viewBox="0 0 14 10" fill="none" stroke="#888" stroke-width="1.2"><rect x=".5" y=".5" width="13" height="9"/><polyline points=".5,.5 7,6 13.5,.5"/></svg>
  <span>enter your email adress</span>
</div>
<div class="abs btn-dark subscribe-btn">SUBSCRIB</div>
<div class="abs social-dot" style="left:493px;background:#1877f2" aria-label="Social link"></div>
<div class="abs social-dot" style="left:550px;background:#1da1f2" aria-label="Social link"></div>
<div class="abs social-dot" style="left:606px;background:#b03ad6" aria-label="Social link"></div>
<div class="abs social-dot" style="left:663px;background:#e4403a" aria-label="Social link"></div>
<p class="abs copyright">© 2019 <b>Elise Marwood</b>. All Right Reserved.</p>

</body>
</html>
```